Vent doux

Hello,
I’m a designer sunglasses reatail Store owner in Montreal, Quebec.

Looking for something modern, fresh with a trendy appeal.

Will send my logo.
Thank you.

Store

```html
<!DOCTYPE html>
<html lang="en">
<head>
<meta charset="utf-8">
<title>Vent doux – business cards</title>
<link rel="stylesheet" href="https://fonts.googleapis.com/css2?family=Lato:wght@300;400;700&display=swap">
<style>
  :root {
    --stage: #e6e4e1;
    --card-white: #f4f4f3;
    --card-black: #231f20;
    --brand-red: #c8102e;
    --ink: #2b2b2b;
    --muted: #6d6d6d;
    --light-text: #f2f2f2;
  }
  * { box-sizing: border-box; margin: 0; padding: 0; }
  html, body { width: 1200px; height: 780px; overflow: hidden; }
  body {
    background: var(--stage);
    font-family: "Lato", Arial, sans-serif;
    position: relative;
  }
  .card {
    position: absolute;
    width: 520px;
    height: 300px;
    top: 240px;
    border-radius: 3px;
    overflow: hidden;
    box-shadow: 0 6px 18px rgba(0,0,0,0.18);
    background: var(--card-white);
  }
  .card-front { left: 40px; }
  .card-back { left: 640px; }
  .card-shape { position: absolute; inset: 0; }

  .wordmark { position: absolute; display: flex; flex-direction: column; }
  .wordmark-name {
    font-weight: 700;
    color: var(--ink);
    letter-spacing: 0.08em;
    text-transform: uppercase;
    line-height: 1;
    white-space: nowrap;
  }
  .wordmark-rule { height: 2px; background: var(--brand-red); margin: 6px 0 5px; }
  .wordmark-tagline {
    font-weight: 300;
    color: var(--muted);
    letter-spacing: 0.14em;
    line-height: 1;
    white-space: nowrap;
  }
  .card-front .wordmark { left: 150px; top: 30px; }
  .card-front .wordmark-name { font-size: 34px; }
  .card-front .wordmark-tagline { font-size: 13px; }

  .card-back .wordmark-row {
    position: absolute; left: 0; right: 0; top: 112px;
    display: flex; justify-content: center; align-items: flex-start; gap: 16px;
  }
  .card-back .wordmark { position: static; }
  .card-back .wordmark-name { font-size: 44px; }
  .card-back .wordmark-tagline { font-size: 15px; }
  .brand-dot {
    width: 22px; height: 22px; border-radius: 50%;
    border: 3px solid var(--brand-red); margin-top: 10px;
  }

  .person { position: absolute; left: 34px; top: 222px; }
  .person-name { font-size: 20px; font-weight: 700; color: var(--light-text); line-height: 1.2; }
  .person-role { font-size: 14px; color: var(--brand-red); margin-top: 2px; }

  .contact {
    position: absolute; left: 262px; top: 190px;
    font-size: 13px; line-height: 19px; color: var(--light-text);
    list-style: none;
  }
  .contact-line { display: flex; align-items: center; gap: 8px; white-space: nowrap; }
  .contact-icon {
    flex: none; width: 12px; height: 12px; border-radius: 50%;
    border: 2px solid var(--brand-red);
  }
  .contact-icon-blank { border-color: transparent; }

  .social { position: absolute; right: 30px; top: 112px; display: flex; gap: 4px; }
  .social-square { width: 16px; height: 16px; background: var(--brand-red); border-radius: 2px; }
</style>
</head>
<body>
  <section class="card card-front" aria-label="Business card front">
    <svg class="card-shape" width="520" height="300" viewBox="0 0 520 300">
      <path d="M0,175 C140,200 290,170 390,112 C445,82 490,70 520,66" fill="none" stroke="var(--brand-red)" stroke-width="7"/>
      <path d="M0,300 L0,185 C140,210 290,180 390,122 C445,92 490,80 520,76 L520,300 Z" fill="var(--card-black)"/>
    </svg>
    <div class="wordmark">
      <span class="wordmark-name">Vent doux</span>
      <span class="wordmark-rule"></span>
      <span class="wordmark-tagline">lunettes &amp; accessoires</span>
    </div>
    <div class="social" aria-label="Social links">
      <span class="social-square"></span><span class="social-square"></span><span class="social-square"></span>
    </div>
    <div class="person">
      <p class="person-name">Lucas Bernier</p>
      <p class="person-role">Founder</p>
    </div>
    <ul class="contact">
      <li class="contact-line"><span class="contact-icon contact-icon-blank"></span>PO Box 88, 410 rue Laurier</li>
      <li class="contact-line"><span class="contact-icon contact-icon-blank"></span>Montreal, Quebec</li>
      <li class="contact-line"><span class="contact-icon"></span>(514) 555-0172</li>
      <li class="contact-line"><span class="contact-icon"></span>hello@ventdoux.ca</li>
      <li class="contact-line"><span class="contact-icon"></span>www.ventdoux.ca</li>
    </ul>
  </section>

  <section class="card card-back" aria-label="Business card back">
    <div class="wordmark-row">
      <span class="brand-dot"></span>
      <div class="wordmark">
        <span class="wordmark-name">Vent doux</span>
        <span class="wordmark-rule"></span>
        <span class="wordmark-tagline">lunettes &amp; accessoires</span>
      </div>
    </div>
  </section>
</body>
</html>
```